Design for large signage in retail outlet.

For a souvenir / gift shop, needing the design for a large sign for the hair braiding section of the shop. Needs to say
"Sunshine Lagoons Hair Braiding " plus pics / background
Bright, sparkly, colourful, eye catching, catering more for women and girls.
A combination of the file 1 and 2, I've supplied. File 3 is what I created, but did not like it. File 4 is typical off the braids we offer.

```html
<!DOCTYPE html>
<html lang="en">
<head>
<meta charset="utf-8">
<title>Sunshine Lagoons Hair Braiding – Sign</title>
<link rel="stylesheet" href="https://fonts.googleapis.com/css2?family=Bebas+Neue&family=Dancing+Script:wght@700&family=Yellowtail&display=block">
<style>
  :root {
    --bg-deep: #0b0408;
    --bg-plum: #2e0a22;
    --bg-magenta: #4f0f3c;
    --silver-light: #f4f8fc;
    --silver-mid: #b9c6d6;
    --silver-dark: #5f6f84;
    --outline: #8a9db3;
    --script-pink: #e23fd6;
    --braids-warm-1: #7a4a2a;
    --braids-warm-2: #c2582e;
    --braids-warm-3: #2c6f8a;
    --braids-bright-1: #d8264a;
    --braids-bright-2: #3a5fd0;
    --braids-bright-3: #8b3cc4;
  }
  html, body {
    margin: 0;
    padding: 0;
    width: 1200px;
    height: 415px;
    overflow: hidden;
    background: var(--bg-deep);
  }
  .sign {
    position: relative;
    width: 1200px;
    height: 415px;
    overflow: hidden;
    background:
      radial-gradient(ellipse 55% 60% at 50% 25%, var(--bg-magenta) 0%, transparent 70%),
      radial-gradient(ellipse 80% 60% at 50% 90%, var(--bg-plum) 0%, transparent 75%),
      linear-gradient(180deg, #1e0716 0%, var(--bg-deep) 55%, #160512 100%);
  }
  .photo {
    position: absolute;
    top: 0;
    height: 415px;
  }
  .photo--left {
    left: 0;
    width: 210px;
    background:
      radial-gradient(ellipse 70% 50% at 30% 35%, var(--braids-warm-2) 0%, transparent 70%),
      radial-gradient(ellipse 60% 50% at 50% 75%, var(--braids-warm-3) 0%, transparent 70%),
      linear-gradient(160deg, var(--braids-warm-1) 0%, #4a2a1c 60%, #2a1410 100%);
    -webkit-mask-image: linear-gradient(90deg, #000 75%, transparent 100%);
            mask-image: linear-gradient(90deg, #000 75%, transparent 100%);
  }
  .photo--right {
    right: 0;
    width: 250px;
    background:
      radial-gradient(ellipse 55% 40% at 60% 15%, var(--braids-bright-1) 0%, transparent 70%),
      radial-gradient(ellipse 40% 60% at 25% 70%, var(--braids-bright-2) 0%, transparent 70%),
      radial-gradient(ellipse 40% 55% at 80% 75%, var(--braids-bright-3) 0%, transparent 70%),
      linear-gradient(180deg, #5a2a4a 0%, #3a1a38 100%);
    -webkit-mask-image: linear-gradient(270deg, #000 78%, transparent 100%);
            mask-image: linear-gradient(270deg, #000 78%, transparent 100%);
  }
  .title-art {
    position: absolute;
    left: 0;
    top: 0;
    width: 1200px;
    height: 415px;
  }
  .title-main {
    font-family: "Bebas Neue", "Oswald", sans-serif;
    font-size: 152px;
  }
  .title-script {
    font-family: "Yellowtail", "Dancing Script", cursive;
    font-size: 100px;
    font-weight: 400;
  }
</style>
</head>
<body>
<main class="sign">
  <div class="photo photo--left" role="img" aria-label="Photo of a woman with long multicoloured box braids, seen from the side"></div>
  <div class="photo photo--right" role="img" aria-label="Portrait of a young woman with rainbow coloured braids"></div>

  <svg class="title-art" viewBox="0 0 1200 415" xmlns="http://www.w3.org/2000/svg">
    <defs>
      <linearGradient id="silverFill" x1="0" y1="0" x2="0.25" y2="1">
        <stop offset="0" stop-color="#f4f8fc"/>
        <stop offset="0.35" stop-color="#b9c6d6"/>
        <stop offset="0.55" stop-color="#f4f8fc"/>
        <stop offset="0.8" stop-color="#5f6f84"/>
        <stop offset="1" stop-color="#f4f8fc"/>
      </linearGradient>
      <linearGradient id="reflectFade" x1="0" y1="0" x2="0" y2="1">
        <stop offset="0" stop-color="#fff" stop-opacity="0.5"/>
        <stop offset="1" stop-color="#fff" stop-opacity="0"/>
      </linearGradient>
      <mask id="reflectMask" maskUnits="userSpaceOnUse" x="0" y="242" width="1200" height="173">
        <rect x="0" y="242" width="1200" height="120" fill="url(#reflectFade)"/>
      </mask>
    </defs>

    <g class="title-reflection" mask="url(#reflectMask)">
      <g transform="translate(0 486) scale(1 -1)">
        <text class="title-main" x="217" y="242" textLength="766" lengthAdjust="spacingAndGlyphs"
              fill="url(#silverFill)" stroke="#8a9db3" stroke-width="2">SUNSHINE LAGOONS</text>
      </g>
    </g>

    <text class="title-main" x="217" y="242" textLength="766" lengthAdjust="spacingAndGlyphs"
          fill="url(#silverFill)" stroke="#8a9db3" stroke-width="2.5">SUNSHINE LAGOONS</text>

    <text class="title-script" x="610" y="296" text-anchor="middle" textLength="460" lengthAdjust="spacingAndGlyphs"
          font-family="Yellowtail, 'Dancing Script', cursive"
          fill="#e23fd6">Hair Braiding</text>
  </svg>
</main>
</body>
</html>
```